Personal Training card design

i am a enthusiastic personal trainer wanting to appeal to as many people as possible.

offering health screening, single or group personal training, geared towards helping the client achieve their goal no matter what it is.

providing a professional service in a top gym facility.

I want to come across professional and trustworthy.

I want my card to be timeless and not look out of date in a years time.

I want the card to be informative and clear about what I offer and display my contact details.

ideally id like the colours blue and white but open to other colour options.

I want the final outcome to communicate professionalism, a PT the clients can trust, and that I can do what I claim.

id like a logo similar to the picture I have provided (the logo on the left hand side) if possible incorporating my initials "OD" or "ODF" but not essential.

Industry/Entity Type

Professional Service

Contact Information for Business Card

OwenDaleyFitness

"Real Results For Every Body"

specializing in
- weight loss & tone
- strength and conditioning
- nutritional advice

Book your free consultation today and take the first step toward achieving your goal!

for details contact me via
email: owendaleyfitness.example.co.uk
phone: 07700954218

or..
visit me via
facebook: owendaleyfitness
twitter: @owendaleyfitness

```html
<!DOCTYPE html>
<html lang="en">
<head>
<meta charset="utf-8">
<title>Owen Daley Fitness – Business Card</title>
<link rel="stylesheet" href="https://fonts.googleapis.com/css2?family=Open+Sans:wght@400;600;700&display=swap">
<style>
  :root {
    --page-bg: #e9edf0;
    --blue-light: #a3e0f7;
    --blue-mid: #5cc3ee;
    --blue-deep: #2a9fdc;
    --white: #ffffff;
    --ink: #3a3a3a;
    --ink-soft: #5a5a5a;
    --tint: #cfeafa;
    --shadow: rgba(20, 40, 60, 0.18);
  }
  * { margin: 0; padding: 0; box-sizing: border-box; }
  html, body { width: 1200px; height: 900px; overflow: hidden; }
  body {
    background: var(--page-bg);
    font-family: "Open Sans", sans-serif;
    position: relative;
  }
  .card {
    position: absolute;
    width: 540px;
    height: 318px;
    border-radius: 4px;
    box-shadow: 0 10px 28px var(--shadow);
    overflow: hidden;
  }

  /* Front */
  .card-front {
    left: 50px;
    top: 110px;
    background: linear-gradient(135deg, var(--blue-light) 0%, var(--blue-mid) 45%, var(--blue-deep) 100%);
    color: var(--white);
  }
  .brand-mark {
    position: absolute;
    left: 42px;
    top: 118px;
    display: flex;
    align-items: center;
    gap: 10px;
  }
  .brand-mark .dot {
    width: 30px; height: 30px;
    border-radius: 50%;
    background: var(--white);
  }
  .brand-mark .initials {
    font-weight: 700;
    font-size: 34px;
    letter-spacing: 1px;
    color: var(--white);
  }
  .brand-name {
    position: absolute;
    left: 190px;
    top: 108px;
    font-size: 36px;
    font-weight: 400;
    line-height: 1.1;
    white-space: nowrap;
  }
  .brand-tagline {
    position: absolute;
    left: 232px;
    top: 158px;
    font-size: 17px;
    font-weight: 600;
    letter-spacing: 0.5px;
    white-space: nowrap;
  }

  /* Back */
  .card-back {
    left: 610px;
    top: 470px;
    background: var(--white);
    color: var(--ink);
  }
  .back-watermark {
    position: absolute;
    left: 150px;
    top: 150px;
    width: 200px;
    height: 200px;
    border-radius: 50%;
    background: var(--tint);
    opacity: 0.6;
  }
  .back-watermark-name {
    position: absolute;
    left: 190px;
    top: 228px;
    font-size: 46px;
    font-weight: 700;
    color: var(--white);
  }
  .services {
    position: absolute;
    left: 0; right: 0;
    top: 26px;
    text-align: center;
    font-size: 13px;
    font-weight: 600;
    letter-spacing: 1.3px;
    line-height: 1.5;
    text-transform: uppercase;
    color: var(--ink);
  }
  .services .cta { font-weight: 700; }
  .contact {
    position: absolute;
    left: 26px;
    bottom: 24px;
    font-size: 12.5px;
    font-weight: 700;
    line-height: 1.6;
    color: var(--ink);
  }
  .contact-row { display: flex; align-items: center; gap: 8px; }
  .contact-row svg { width: 13px; height: 13px; fill: var(--ink); flex: none; }
  .contact-row.phone { font-size: 15px; }
  .for-details {
    position: absolute;
    left: 240px;
    top: 208px;
    font-size: 12px;
    font-weight: 700;
    letter-spacing: 1px;
    color: var(--ink-soft);
  }
  .social {
    position: absolute;
    right: 26px;
    top: 152px;
    font-size: 11.5px;
    font-weight: 600;
    line-height: 1.75;
    color: var(--ink);
  }
  .social-row { display: flex; align-items: center; gap: 7px; }
  .social-row .square {
    width: 13px; height: 13px;
    background: var(--blue-deep);
    flex: none;
  }
</style>
</head>
<body>

  <section class="card card-front" aria-label="Business card front">
    <div class="brand-mark">
      <span class="dot"></span>
      <span class="initials">ODF</span>
    </div>
    <h1 class="brand-name">Owen Daley Fitness</h1>
    <p class="brand-tagline">"Real Results For Every Body"</p>
  </section>

  <section class="card card-back" aria-label="Business card back">
    <div class="back-watermark"></div>
    <span class="back-watermark-name">ODF</span>

    <div class="services">
      <p>Specializing in -</p>
      <p>Weight loss &amp; tone</p>
      <p>Strength and conditioning</p>
      <p>Nutritional advice</p>
      <p class="cta">Book your free consultation today</p>
      <p class="cta">&amp; take the first step toward achieving your goal!</p>
    </div>

    <p class="for-details">FOR DETAILS</p>

    <div class="contact">
      <p>contact me via</p>
      <p class="contact-row email">
        <svg viewBox="0 0 16 16" aria-hidden="true"><path d="M1 3h14v10H1z M1.8 3.8 8 8.6l6.2-4.8" fill="none" stroke="#3a3a3a" stroke-width="1.6"/></svg>
        owendaleyfitness.example.co.uk
      </p>
      <p class="contact-row phone">
        <svg viewBox="0 0 16 16" aria-hidden="true"><path d="M3.5 1.5 6 4.2 4.7 6.1c.9 2 2.6 3.7 4.6 4.6l1.9-1.3 2.7 2.5-1.5 2.3C7 14 2 9 1.3 3.2z"/></svg>
        07700954218
      </p>
    </div>

    <div class="social">
      <p>or visit me via</p>
      <p class="social-row"><span class="square"></span>owendaleyfitness</p>
      <p class="social-row"><span class="square"></span>@owendaleyfitness</p>
    </div>
  </section>

</body>
</html>
```